Coastal Rubdown Oil Co. needs a new label.

This massage oil has been in Australia for over 20 years and needs a new label for its plastic 250ml bottles. The current label (8cm x 8cm) looks old fashioned and so we are looking for something that reflects freedom, relaxation, inspiration. The product is made from sweet almond oil and has different essential oils used to give unique smells. I have seen some lovely abstract vector images. I think we need a clean straight look with bright colours. There are currently six variations to the product. "Weary and Worn Heads, Achy and Spent Frames, Couples Mix, Heather Soak Oil, Unwinding Mix, Uplift Mix" Different coloured labels have been used for each of the blends. I have included photos of existing bottles plus some ideas for the labels.

I would like to use the same font on the name of the brand Bramblewick Acres. If we change the font it may be difficult for existing customers to find our product.

Also just under the name Bramblewick Acres I would like to insert a type of logo (can be the shape of a tear drop or round circle) to say:

Massage Oil
Since 1970

The size of the label is 8cm x 12 cm for the front and the same size for the back of the label.
Updates

Coastal Rubdown oil Company has posted on the brief some images from Pixelvault plus two photos of the original bottles. I am looking for a new design which is bright in colour, fun and funky. I am not thinking along the lines of the traditional Herb and trees look. I think the original label is too busy and the colours overpower the label. The other point I think that is important is that the product has been around since 1970. If there is room I think a round logo which says: Massage Oil Since 1970 I am hoping that we can fit this information on the label Looking forward to seeing all the designs come thru. So far I have only had two designs come thru. Speak soon from hot sunny Australia. maree

Thank you to everyone who has already posted designs for our Massage Label. I have now edited the brief to include some more ideas on how to make this design the Best! I will email back to you straight away ideas and thoughts on your designs. Remember I live in Australia and can be either 10hrs in front or behind your time.

Reason: Due to busy lives and commitments over the next few days I feel that an extension will benefit all involved. Thank you to everyone who has submitted designs and working with me to create something beautiful. maree

Hello from Australia all the designers who have submitted some wonderful designs over the past two weeks. We are now entering the final three days of the competition. Thank you to everyone who has worked so hard to try and create the perfect label for my massage oil bottle. All of you have done a fantastic job. This has made the decision hard to make. Thank you to everyone. Please submit all your last minute designs soon. kind regards maree Australia

Target Market(s)

The type of person purchasing a massage oil blend will buy from a health food shop, pharmacy or from an on-line store. I believe they are wanting something bright that clearly communicates that that it is a massage oil.

Industry/Entity Type

Massage

Font styles to use
Script

Requirements
Must have
• Different colour for each massage oil blend.
Need same font for the name Bramblewick Acres. (script font or similar)

Abstract design please.
Nice to have
• A logo under the name Bramblewick Acres

Tear Drop or circle design that says:

Massage Oil
Since 1970

also we would like an outline for the back label. (see photo attached)

BACK LABEL information

A unique blend of essential oils in a fine light base.

Contains:

vegetable oil extract of nettle, sweet almond oil, ethanol, essential oils of lavender, lemongrass, orange & ylang ylang and vitamin E.

How to Use:

Shake well warm bottle in warm water if very cold.
Lovingly massage the body from head to toe.
Not for medicinal use.

Bramblewick Acres
Hollin WA 6099
Phone: (08) 9555 0142

(LEAVE ROOM FOR BARCODE)
Should not have
• Too busy design or old fashioned design.
No dull colours.

```html
<!DOCTYPE html>
<html lang="en">
<head>
<meta charset="utf-8">
<title>Bramblewick Acres Massage Oil Labels</title>
<link href="https://fonts.googleapis.com/css2?family=Playball&family=Crimson+Text:wght@400;700&display=swap" rel="stylesheet">
<style>
  :root {
    --bg-top: #ffffff;
    --bg-bottom: #dcdcdc;
    --ink: #1a1a1a;
    --label-text: #ffffff;
  }
  html, body {
    margin: 0;
    padding: 0;
    width: 1200px;
    height: 873px;
    overflow: hidden;
  }
  body {
    background: linear-gradient(180deg, var(--bg-top) 0%, var(--bg-top) 20%, var(--bg-bottom) 100%);
    position: relative;
  }
  .label-range {
    position: absolute;
    left: 166px;
    top: 384px;
    display: flex;
    gap: 17px;
  }
  .label {
    position: relative;
    width: 128px;
    height: 258px;
    overflow: hidden;
    background: linear-gradient(180deg, var(--tint) 0%, var(--tint) 12%, var(--mid) 45%, var(--deep) 100%);
  }
  .label__pattern {
    position: absolute;
    left: 0;
    right: 0;
    top: 22px;
    bottom: 0;
    background:
      radial-gradient(ellipse at 15% 30%, var(--mid) 0%, transparent 45%),
      radial-gradient(ellipse at 85% 60%, var(--mid) 0%, transparent 45%),
      linear-gradient(180deg, transparent 0%, var(--deep) 100%);
    opacity: 0.85;
  }
  .label__oval {
    position: absolute;
    left: 24px;
    top: 50px;
    width: 80px;
    height: 180px;
    border-radius: 50%;
    background: var(--deep);
    opacity: 0.55;
  }
  .label__brand {
    position: absolute;
    top: 2px;
    left: 0;
    right: 0;
    text-align: center;
    font-family: "Playball", cursive;
    font-size: 15px;
    line-height: 15px;
    color: var(--ink);
  }
  .label__drop {
    position: absolute;
    left: 51px;
    top: 55px;
    width: 26px;
    height: 36px;
  }
  .label__product {
    position: absolute;
    top: 103px;
    left: 0;
    right: 0;
    text-align: center;
    font-family: "Crimson Text", serif;
    font-weight: 700;
    font-size: 13px;
    color: var(--label-text);
  }
  .label__blend {
    position: absolute;
    top: 124px;
    left: 22px;
    right: 22px;
    text-align: center;
    font-family: "Crimson Text", serif;
    font-size: 10px;
    line-height: 14px;
    color: var(--label-text);
  }
  .label__volume {
    position: absolute;
    bottom: 3px;
    left: 0;
    right: 0;
    text-align: center;
    font-family: "Crimson Text", serif;
    font-weight: 700;
    font-size: 6px;
    color: var(--label-text);
  }
  .label--couples { --tint: #ffc4c4; --mid: #e04a3a; --deep: #a3150c; }
  .label--frames  { --tint: #ffd4a6; --mid: #d98224; --deep: #9c4a10; }
  .label--heather { --tint: #ebbcf4; --mid: #a444c4; --deep: #6e0f9e; }
  .label--heads   { --tint: #b6eeaa; --mid: #62c240; --deep: #2f8010; }
  .label--unwind  { --tint: #fff0a4; --mid: #d2b224; --deep: #9a7e04; }
  .label--uplift  { --tint: #ffd8bc; --mid: #e0602e; --deep: #b0280a; }
</style>
</head>
<body>
  <main class="label-range">
    <article class="label label--couples">
      <div class="label__pattern" role="img" aria-label="Abstract leaf pattern in red tones"></div>
      <div class="label__oval"></div>
      <div class="label__brand">Bramblewick<br>Acres</div>
      <svg class="label__drop" viewBox="0 0 26 36"><path d="M13 1 C13 1 2 18 2 24 a11 11 0 0 0 22 0 C24 18 13 1 13 1Z" fill="#ffffff" opacity="0.85"/></svg>
      <div class="label__product">Massage Oil</div>
      <div class="label__blend">Couples Mix.</div>
      <div class="label__volume">250 ml</div>
    </article>
    <article class="label label--frames">
      <div class="label__pattern" role="img" aria-label="Abstract leaf pattern in orange tones"></div>
      <div class="label__oval"></div>
      <div class="label__brand">Bramblewick<br>Acres</div>
      <svg class="label__drop" viewBox="0 0 26 36"><path d="M13 1 C13 1 2 18 2 24 a11 11 0 0 0 22 0 C24 18 13 1 13 1Z" fill="#ffffff" opacity="0.85"/></svg>
      <div class="label__product">Massage Oil</div>
      <div class="label__blend">for Achy and Spent Frames.</div>
      <div class="label__volume">250 ml</div>
    </article>
    <article class="label label--heather">
      <div class="label__pattern" role="img" aria-label="Abstract leaf pattern in purple tones"></div>
      <div class="label__oval"></div>
      <div class="label__brand">Bramblewick<br>Acres</div>
      <svg class="label__drop" viewBox="0 0 26 36"><path d="M13 1 C13 1 2 18 2 24 a11 11 0 0 0 22 0 C24 18 13 1 13 1Z" fill="#ffffff" opacity="0.85"/></svg>
      <div class="label__product">Massage Oil</div>
      <div class="label__blend">Heather Soak Oil.</div>
      <div class="label__volume">250 ml</div>
    </article>
    <article class="label label--heads">
      <div class="label__pattern" role="img" aria-label="Abstract leaf pattern in green tones"></div>
      <div class="label__oval"></div>
      <div class="label__brand">Bramblewick<br>Acres</div>
      <svg class="label__drop" viewBox="0 0 26 36"><path d="M13 1 C13 1 2 18 2 24 a11 11 0 0 0 22 0 C24 18 13 1 13 1Z" fill="#ffffff" opacity="0.85"/></svg>
      <div class="label__product">Massage Oil</div>
      <div class="label__blend">for Weary and Worn Heads.</div>
      <div class="label__volume">250 ml</div>
    </article>
    <article class="label label--unwind">
      <div class="label__pattern" role="img" aria-label="Abstract leaf pattern in yellow tones"></div>
      <div class="label__oval"></div>
      <div class="label__brand">Bramblewick<br>Acres</div>
      <svg class="label__drop" viewBox="0 0 26 36"><path d="M13 1 C13 1 2 18 2 24 a11 11 0 0 0 22 0 C24 18 13 1 13 1Z" fill="#ffffff" opacity="0.85"/></svg>
      <div class="label__product">Massage Oil</div>
      <div class="label__blend">Unwinding Mix.</div>
      <div class="label__volume">250 ml</div>
    </article>
    <article class="label label--uplift">
      <div class="label__pattern" role="img" aria-label="Abstract leaf pattern in orange-red tones"></div>
      <div class="label__oval"></div>
      <div class="label__brand">Bramblewick<br>Acres</div>
      <svg class="label__drop" viewBox="0 0 26 36"><path d="M13 1 C13 1 2 18 2 24 a11 11 0 0 0 22 0 C24 18 13 1 13 1Z" fill="#ffffff" opacity="0.85"/></svg>
      <div class="label__product">Massage Oil</div>
      <div class="label__blend">Uplift Mix.</div>
      <div class="label__volume">250 ml</div>
    </article>
  </main>
</body>
</html>
```